new signage design for budget motel - Brookfern Lodge

renaming the budget motel as Brookfern Lodge, property located on side of a hill. therefore i choose to name is Brookfern Lodge, im looking for clean, modern look in signage design,this property does not have a Logo, plan to us signage design as a logo as well. current pole sign housing is rectangle shape and will be using same housing I'll be attaching picture of the signage for better idea. looking forward to awesome creative designs.

Industry/Entity Type

Motel

Font styles to use
Serif
Sans Serif

Requirements
Should not have
• mountains , mountain(s) with snow , trees, no black color, red color, blue letters, too much green.

```html
<!DOCTYPE html>
<html lang="en">
<head>
<meta charset="utf-8">
<title>Brookfern Lodge — Pole Sign</title>
<link rel="stylesheet" href="https://fonts.googleapis.com/css2?family=Kaushan+Script&family=Josefin+Sans:wght@400&display=swap">
<style>
  :root {
    --page-bg: #f2f2f2;
    --wood-light: #c0825a;
    --wood-mid: #ad6f48;
    --wood-dark: #9a5f3c;
    --ink: #2e1204;
    --shadow: rgba(0, 0, 0, 0.22);
  }
  * { margin: 0; padding: 0; box-sizing: border-box; }
  html, body {
    width: 800px;
    height: 1200px;
    overflow: hidden;
    background: var(--page-bg);
  }
  .canvas {
    position: relative;
    width: 800px;
    height: 1200px;
  }
  .sign-board {
    position: absolute;
    left: 40px;
    top: 330px;
    width: 720px;
    height: 540px;
    box-shadow: 0 4px 14px var(--shadow);
    overflow: hidden;
  }
  .wood-surface {
    position: absolute;
    inset: 0;
    width: 100%;
    height: 100%;
  }
  .sign-frame {
    position: absolute;
    left: 27px;
    top: 25px;
    right: 27px;
    bottom: 25px;
    border: 4px solid var(--ink);
  }
  .sign-name {
    position: absolute;
    left: 0;
    right: 0;
    top: 70px;
    text-align: center;
    font-family: "Kaushan Script", cursive;
    font-size: 118px;
    line-height: 1.3;
    color: var(--ink);
  }
  .sign-subtitle {
    position: absolute;
    left: 50%;
    top: 335px;
    width: 340px;
    height: 158px;
    transform: translateX(-50%);
    border-top: 1.5px solid var(--ink);
    border-bottom: 1.5px solid var(--ink);
    display: flex;
    align-items: center;
    justify-content: center;
    font-family: "Josefin Sans", sans-serif;
    font-weight: 400;
    font-size: 96px;
    letter-spacing: 8px;
    padding-top: 14px;
    padding-left: 8px;
    color: var(--ink);
  }
</style>
</head>
<body>
  <main class="canvas">
    <section class="sign-board">
      <svg class="wood-surface" role="img" aria-label="Warm brown wood grain surface" viewBox="0 0 720 540" preserveAspectRatio="none">
        <defs>
          <linearGradient id="woodTone" x1="0" y1="0" x2="0" y2="1">
            <stop offset="0" stop-color="var(--wood-mid)"/>
            <stop offset="0.35" stop-color="var(--wood-light)"/>
            <stop offset="0.6" stop-color="var(--wood-mid)"/>
            <stop offset="1" stop-color="var(--wood-dark)"/>
          </linearGradient>
        </defs>
        <rect width="720" height="540" fill="url(#woodTone)"/>
      </svg>
      <div class="sign-frame"></div>
      <h1 class="sign-name">Brookfern</h1>
      <p class="sign-subtitle">LODGE</p>
    </section>
  </main>
</body>
</html>
```